Brightwall painting and decorating *

Need a flyer design to advertise my services
So the information I need included is the services we offer at brightwall painting and decorating which include
Interior painting
Exterior painting
Wallpaper hanging
Paint and cellulose spraying
Dust free sanding
Pressure washing
Stone cleaning
Also would need to have my company contact details in
Www.brightwallpaintingdecorating.co.uk
Email is info@brightwallpaintingdecorating.com
Brightwall Painting & Decorating Services has a proven track record of innovative designs, effective problem solving and attention to detail and our goal is to meet and exceed the expectations of every customer. We take on all types of jobs from small domestic work to larger commercial projects, all carried out to the highest standards, and at very competitive prices.
Colors
Designer to choose colors to be used in the design.
Look and feel

```html
<!DOCTYPE html>
<html lang="en">
<head>
<meta charset="utf-8">
<title>Brightwall Painting and Decorating – Flyer</title>
<link href="https://fonts.googleapis.com/css2?family=Open+Sans:wght@400;600;700;800&display=swap" rel="stylesheet">
<style>
  :root {
    --navy: #0a4a7c;
    --heading: #0d4f86;
    --sky: #2b86c9;
    --white: #ffffff;
    --footer: #464646;
    --text-on-photo: #ffffff;
  }
  * { margin: 0; padding: 0; box-sizing: border-box; }
  html, body { width: 818px; height: 1200px; overflow: hidden; background: #e6e6e6; }
  .flyer {
    position: relative; width: 818px; height: 1200px; overflow: hidden;
    font-family: "Open Sans", Arial, sans-serif; background: var(--white);
  }
  .flyer-art { position: absolute; inset: 0; }
  .brand { position: absolute; left: 56px; top: 64px; width: 250px; text-align: center; }
  .brand-name { font-size: 40px; font-weight: 800; color: var(--navy); letter-spacing: 0.5px; line-height: 1; }
  .brand-tagline { font-size: 11.6px; font-weight: 600; color: var(--sky); margin-top: 6px; white-space: nowrap; }
  .hero { position: absolute; left: 52px; top: 284px; width: 350px; color: var(--text-on-photo); }
  .hero-title { font-size: 29px; font-weight: 800; line-height: 1.1; }
  .hero-sub { font-size: 29px; font-weight: 400; line-height: 1.15; }
  .hero-text { font-size: 14.2px; line-height: 1.27; margin-top: 10px; }
  .services { position: absolute; left: 62px; color: var(--heading); }
  .services h2 { font-size: 23.5px; font-weight: 600; margin-bottom: 8px; }
  .services ul { list-style: none; margin-left: 3px; }
  .services li { font-size: 17.6px; line-height: 25.9px; }
  .services.domestic { top: 533px; }
  .services.commercial { top: 742px; left: 60px; }
  .about { position: absolute; left: 62px; top: 890px; width: 400px; font-size: 13px; line-height: 1.42; color: var(--heading); }
  .contact { position: absolute; right: 319px; top: 1078px; text-align: right; color: var(--white); line-height: 1.35; }
  .contact-label { font-size: 14px; }
  .contact-phone { font-size: 21.5px; line-height: 1.3; }
  .contact-email, .contact-web { font-size: 14px; }
</style>
</head>
<body>
<div class="flyer">
  <svg class="flyer-art" width="818" height="1200" viewBox="0 0 818 1200" xmlns="http://www.w3.org/2000/svg">
    <defs>
      <linearGradient id="kitchenTone" x1="0" y1="0" x2="1" y2="1">
        <stop offset="0" stop-color="#a9a6a2"/>
        <stop offset="0.45" stop-color="#7a7876"/>
        <stop offset="1" stop-color="#c9c6c1"/>
      </linearGradient>
      <linearGradient id="yellowRoom" x1="0" y1="0" x2="1" y2="1">
        <stop offset="0" stop-color="#f2c04a"/><stop offset="1" stop-color="#f5d27a"/>
      </linearGradient>
      <linearGradient id="navyRoom" x1="0" y1="0" x2="1" y2="1">
        <stop offset="0" stop-color="#2c4a5e"/><stop offset="1" stop-color="#5b4a3e"/>
      </linearGradient>
      <linearGradient id="officeRoom" x1="0" y1="0" x2="1" y2="1">
        <stop offset="0" stop-color="#d9e6ec"/><stop offset="1" stop-color="#8fb3c4"/>
      </linearGradient>
      <linearGradient id="loungeRoom" x1="0" y1="0" x2="0" y2="1">
        <stop offset="0" stop-color="#e6e9e8"/><stop offset="1" stop-color="#9c968c"/>
      </linearGradient>
      <filter id="softShadow" x="-20%" y="-20%" width="140%" height="140%">
        <feDropShadow dx="0" dy="3" stdDeviation="5" flood-color="#000" flood-opacity="0.3"/>
      </filter>
    </defs>

    <rect class="hero-photo" x="0" y="40" width="818" height="760" fill="url(#kitchenTone)" role="img" aria-label="Photo of a modern grey kitchen with dining table and chairs"/>

    <path class="lower-panel" d="M0,473 C230,455 440,520 545,690 L600,690 L600,1200 L0,1200 Z" fill="var(--white)"/>
    <path class="footer-band" d="M0,1112 C200,1140 400,1080 560,990 L620,1200 L0,1200 Z" fill="var(--footer)"/>

    <path class="accent-band" d="M818,60 L818,1200 L570,1200 C610,1160 600,1020 560,880 C520,740 500,600 520,420 C540,260 640,110 818,60 Z" fill="var(--sky)"/>
    <path class="side-panel" d="M818,90 L818,1200 L598,1200 C605,1050 600,930 605,860 C610,700 605,480 625,360 C645,230 700,140 818,90 Z" fill="var(--navy)"/>

    <path class="top-stripe" d="M0,180 C120,250 250,230 430,150 C600,75 720,60 818,70 L818,82 C720,80 600,100 430,175 C260,250 120,255 0,215 Z" fill="var(--sky)"/>
    <path class="top-panel" d="M0,0 L818,0 L818,70 C720,60 600,75 430,150 C250,230 120,250 0,189 Z" fill="var(--white)"/>

    <rect x="56" y="134" width="85" height="1.4" fill="var(--navy)"/>
    <rect x="146" y="128" width="76" height="13" rx="6.5" fill="var(--navy)" opacity="0.18" role="img" aria-label="Decorative flourish"/>
    <rect x="227" y="134" width="80" height="1.4" fill="var(--navy)"/>

    <g filter="url(#softShadow)" fill="var(--white)">
      <circle cx="629" cy="226" r="108"/>
      <circle cx="555" cy="481" r="108"/>
      <circle cx="603" cy="747" r="108"/>
      <circle cx="603" cy="1027" r="108"/>
    </g>
    <circle cx="629" cy="226" r="88" fill="url(#yellowRoom)" role="img" aria-label="Photo of a yellow living room with sofa and plant"/>
    <circle cx="555" cy="481" r="88" fill="url(#navyRoom)" role="img" aria-label="Photo of a navy blue study with fireplace"/>
    <circle cx="603" cy="747" r="88" fill="url(#officeRoom)" role="img" aria-label="Photo of a bright office with textured feature wall"/>
    <circle cx="603" cy="1027" r="88" fill="url(#loungeRoom)" role="img" aria-label="Photo of a commercial lounge with grey armchairs"/>

    <rect x="65" y="707" width="90" height="1.6" fill="var(--navy)"/>
    <rect x="160" y="698" width="150" height="18" rx="9" fill="var(--navy)" opacity="0.18" role="img" aria-label="Decorative flourish divider"/>
    <rect x="315" y="707" width="83" height="1.6" fill="var(--navy)"/>

    <g class="social-dots" role="img" aria-label="Social media links">
      <circle cx="54" cy="1152" r="12" fill="#3b5a9a"/>
      <circle cx="89" cy="1152" r="12" fill="#1d9bd9"/>
      <circle cx="122" cy="1152" r="12" fill="#1270b0"/>
      <circle cx="158" cy="1152" r="12" fill="#3bb44a"/>
      <circle cx="193" cy="1152" r="12" fill="#7c7c7c"/>
    </g>
  </svg>

  <div class="brand">
    <div class="brand-name">BRIGHTWALL</div>
    <div class="brand-tagline">PAINTING AND DECORATING SERVICES</div>
  </div>

  <div class="hero">
    <div class="hero-title">Established decorators</div>
    <div class="hero-sub">in South London</div>
    <p class="hero-text">Get in touch with our expert decorators at Brightwall Painting and Decorating Services in Bexley to give your property a makeover. Our services are available across South London.</p>
  </div>

  <section class="services domestic">
    <h2>Domestic Services</h2>
    <ul>
      <li>Interior painting</li>
      <li>Exterior painting</li>
      <li>Wallpaper hanging</li>
      <li>Stone cleaning</li>
    </ul>
  </section>

  <section class="services commercial">
    <h2>Commercial Services</h2>
    <ul>
      <li>Paint and cellulose spraying</li>
      <li>Dust free sanding</li>
      <li>Pressure washing</li>
    </ul>
  </section>

  <p class="about">Brightwall Painting &amp; Decorating Services has a proven track record of innovative designs, effective problem solving and attention to detail and our goal is to meet and exceed the expectations of every customer. We take on all types of jobs from small domestic work to larger commercial projects, all carried out to the highest standards, and at very competitive prices.</p>

  <div class="contact">
    <div class="contact-label">free quote</div>
    <div class="contact-phone">07700 900 416</div>
    <div class="contact-email">info@brightwallpaintingdecorating.com</div>
    <div class="contact-web">www.brightwallpaintingdecorating.co.uk</div>
  </div>
</div>
</body>
</html>
```